Bref créative
Business Cards and Letterhead
85 mm x 55 mm / DIN A4 210 mm × 297 mm
Professional
Dominik R. Hartl
Lindenweg 7, 14471 Potsdam
info@lbr-planung.example
www.lbr-planung.example
Please use the standard german sizes for business cards and letters:
85 mm x 55 mm
DIN A4: 210 mm × 297 mm

```html
<!DOCTYPE html>
<html lang="de">
<head>
<meta charset="utf-8">
<title>lbrplanung – Visitenkarten</title>
<link rel="stylesheet" href="https://fonts.googleapis.com/css2?family=Open+Sans:wght@400;600;700;800&display=swap">
<style>
  :root {
    --orange: #f6a04d;
    --orange-deep: #ef8f32;
    --ink: #1c1c1c;
    --paper: #f7f7f7;
    --paper-shade: #e4e4e4;
    --night: #0c0c0c;
    --stage-light: #8d8d8d;
    --stage-dark: #333333;
    --swoosh: #c9c9c9;
  }
  * { box-sizing: border-box; margin: 0; padding: 0; }
  html, body { width: 1200px; height: 713px; overflow: hidden; }
  body {
    font-family: "Open Sans", Arial, sans-serif;
    background: radial-gradient(ellipse at 50% 45%, var(--stage-light) 0%, #6a6a6a 45%, var(--stage-dark) 100%);
    position: relative;
  }
  .card {
    position: absolute;
    width: 530px;
    height: 295px;
    border-radius: 14px;
    overflow: hidden;
    box-shadow: 0 3px 10px rgba(0,0,0,.35);
  }
  .card--front { left: 53px; top: 48px; background: linear-gradient(180deg, #ffffff 0%, var(--paper) 60%, var(--paper-shade) 100%); }
  .card--light { left: 619px; top: 48px; background: linear-gradient(160deg, #ffffff 0%, var(--paper) 55%, var(--paper-shade) 100%); }
  .card--orange { left: 53px; top: 372px; background: linear-gradient(160deg, #f8ab5f 0%, var(--orange) 55%, var(--orange-deep) 100%); }
  .card--dark { left: 619px; top: 372px; background: linear-gradient(160deg, #1b1b1b 0%, var(--night) 100%); }

  .front-band { position: absolute; inset: 0; width: 530px; height: 295px; }
  .holder-name {
    position: absolute; right: 28px; top: 14px;
    font-size: 27px; font-weight: 700; color: var(--ink); letter-spacing: -.2px;
  }
  .brand { position: absolute; display: flex; flex-direction: column; }
  .brand__row { display: flex; align-items: center; gap: 10px; }
  .brand__mark { width: 16px; height: 16px; background: var(--orange); flex: none; }
  .brand__name { font-size: 44px; font-weight: 800; line-height: 1; letter-spacing: -1px; }
  .brand__tagline { font-size: 10.5px; font-weight: 600; margin-top: 4px; letter-spacing: .1px; }

  .card--front .brand { left: 26px; top: 102px; }
  .card--front .brand__name, .card--front .brand__tagline { color: var(--ink); }

  .contact {
    position: absolute; left: 26px; top: 180px;
    list-style: none; font-size: 12.5px; line-height: 16px; color: #333;
  }

  .backdrop-name {
    position: absolute; left: 40px; top: -20px;
    font-size: 200px; font-weight: 800; letter-spacing: -6px; line-height: 1;
  }
  .card--light .backdrop-name { color: rgba(0,0,0,.07); }
  .card--orange .backdrop-name { color: rgba(255,255,255,.13); }
  .card--dark .backdrop-name { color: rgba(255,255,255,.09); }

  .card--light .brand, .card--orange .brand, .card--dark .brand { right: 28px; bottom: 30px; align-items: flex-end; }
  .card--light .brand__name, .card--light .brand__tagline { color: var(--ink); }
  .card--orange .brand__name, .card--orange .brand__tagline,
  .card--dark .brand__name, .card--dark .brand__tagline { color: #ffffff; }
  .card--orange .brand__mark { background: #ffffff; }
</style>
</head>
<body>

  <section class="card card--front" aria-label="Vorderseite">
    <svg class="front-band" viewBox="0 0 530 295" aria-hidden="true">
      <path d="M150 0 H530 V108 C420 70 300 55 150 0 Z" fill="var(--orange)"/>
      <path d="M0 70 C150 40 330 70 530 118 V124 C330 80 150 52 0 78 Z" fill="var(--swoosh)"/>
    </svg>
    <h1 class="holder-name">Dominik R. Hartl</h1>
    <div class="brand">
      <div class="brand__row"><span class="brand__mark"></span><span class="brand__name">lbrplanung</span></div>
      <span class="brand__tagline">Unternehmensberatung · Coaching · Seminare</span>
    </div>
    <ul class="contact">
      <li>Lindenweg 7, 14471 Potsdam</li>
      <li>Phone: (0331) 555 18 40-0</li>
      <li>Cell: (0170) 555 02 19</li>
      <li>Fax: (0331) 555 18 40-9</li>
      <li>Email: info@lbr-planung.example</li>
      <li>Web: www.lbr-planung.example</li>
    </ul>
  </section>

  <section class="card card--light" aria-label="Rückseite hell">
    <span class="backdrop-name" aria-hidden="true">LBR</span>
    <div class="brand">
      <div class="brand__row"><span class="brand__mark"></span><span class="brand__name">lbrplanung</span></div>
      <span class="brand__tagline">Unternehmensberatung · Coaching · Seminare</span>
    </div>
  </section>

  <section class="card card--orange" aria-label="Rückseite orange">
    <span class="backdrop-name" aria-hidden="true">LBR</span>
    <div class="brand">
      <div class="brand__row"><span class="brand__mark"></span><span class="brand__name">lbrplanung</span></div>
      <span class="brand__tagline">Unternehmensberatung · Coaching · Seminare</span>
    </div>
  </section>

  <section class="card card--dark" aria-label="Rückseite schwarz">
    <span class="backdrop-name" aria-hidden="true">LBR</span>
    <div class="brand">
      <div class="brand__row"><span class="brand__mark"></span><span class="brand__name">lbrplanung</span></div>
      <span class="brand__tagline">Unternehmensberatung · Coaching · Seminare</span>
    </div>
  </section>

</body>
</html>
```